Kestrel Valley Alpine Riders Society needs a business card design

We need a business card design for our newly incorporated KVARS. We are helping the NZ Chinese community, as well as everyone else, to organise ski & snowboarding trips, training, and equipments. The design should be creative, energetic, young and vibrant.

Industry/Entity Type

Social Club

Contact Information for Business Card

Logo; Kestrel Valley Alpine Riders Society; Name: Oliver Brandt; Position: President; Address: 42 Marwick Rd, Epsom, Auckland 1051; Mobile: 020 7826 1957; Email: oliver@kvars-club.example; Web: www.kvars-club.example

Requirements
Must have
• 1, The text "Kestrel Valley Alpine Riders Society" should be put together with the supplied logo file to form a new complete logo combination.
• 2, Final design files should be in Adobe Illustrator format and all text must be editable.
Nice to have
• two or three colours

```html
<!DOCTYPE html>
<html lang="en">
<head>
<meta charset="utf-8">
<title>KVARS Business Card</title>
<link rel="stylesheet" href="https://fonts.googleapis.com/css2?family=Open+Sans:wght@400;600;700;800&display=swap">
<style>
  :root {
    --bg: #2b2d30;
    --sky-light: #19b3e8;
    --sky-mid: #1b86d6;
    --sky-deep: #1d5fc4;
    --brand-blue: #1e56b4;
    --stripe-light: #16a6e2;
    --stripe-dark: #1d4fae;
    --ink-grey: #6d6f72;
    --paper: #ffffff;
  }
  * { box-sizing: border-box; margin: 0; padding: 0; }
  html, body { width: 1200px; height: 864px; overflow: hidden; }
  body {
    background: var(--bg);
    font-family: "Open Sans", Arial, sans-serif;
    position: relative;
  }
  .card {
    position: absolute;
    left: 290px;
    width: 620px;
    height: 354px;
    box-shadow: 0 14px 30px rgba(0,0,0,0.45);
    overflow: hidden;
  }
  .card--front {
    top: 48px;
    background: radial-gradient(ellipse at 50% 45%, var(--sky-light) 0%, var(--sky-mid) 45%, var(--sky-deep) 100%);
    color: var(--paper);
    text-align: center;
  }
  .front-wordmark {
    position: absolute;
    top: 96px;
    left: 0;
    width: 100%;
    font-size: 74px;
    font-weight: 800;
    letter-spacing: 2px;
    line-height: 1;
    color: var(--paper);
  }
  .front-tagline {
    position: absolute;
    top: 236px;
    left: 0;
    width: 100%;
    font-size: 17px;
    font-weight: 600;
    letter-spacing: 0.3px;
  }
  .card--back {
    top: 462px;
    background: var(--paper);
  }
  .back-wordmark {
    position: absolute;
    top: 38px;
    right: 46px;
    font-size: 46px;
    font-weight: 800;
    letter-spacing: 1.5px;
    color: var(--brand-blue);
    line-height: 1;
  }
  .holder { position: absolute; left: 44px; top: 162px; }
  .holder-name { font-size: 27px; font-weight: 700; color: var(--brand-blue); line-height: 1.1; }
  .holder-role { font-size: 17px; color: var(--ink-grey); margin-top: 2px; }
  .divider {
    position: absolute;
    left: 44px; right: 44px; top: 228px;
    height: 1.5px;
    background: var(--brand-blue);
  }
  .contacts {
    position: absolute;
    left: 48px; top: 240px;
    list-style: none;
    font-size: 16px;
    color: var(--ink-grey);
  }
  .contacts li { display: flex; align-items: center; gap: 9px; height: 24px; }
  .contacts svg { width: 16px; height: 16px; flex: none; }
  .address {
    position: absolute;
    right: 46px; top: 240px;
    text-align: right;
    font-size: 16px;
    color: var(--ink-grey);
    line-height: 1.4;
  }
  .footer-band { position: absolute; left: 0; bottom: 0; width: 620px; height: 22px; }
</style>
</head>
<body>
  <section class="card card--front">
    <div class="front-wordmark">KVARS</div>
    <div class="front-tagline">Kestrel Valley Alpine Riders Society</div>
  </section>

  <section class="card card--back">
    <div class="back-wordmark">KVARS</div>

    <div class="holder">
      <div class="holder-name">Oliver Brandt</div>
      <div class="holder-role">President</div>
    </div>

    <div class="divider"></div>

    <ul class="contacts">
      <li>
        <svg viewBox="0 0 16 16" fill="none" stroke="#1e56b4" stroke-width="1.4"><rect x="4" y="1" width="8" height="14" rx="1.5"/><line x1="7" y1="12.5" x2="9" y2="12.5"/></svg>
        020 7826 1957
      </li>
      <li>
        <svg viewBox="0 0 16 16" fill="none" stroke="#1e56b4" stroke-width="1.4"><rect x="1" y="3.5" width="14" height="9" rx="1"/><polyline points="1,4 8,9.5 15,4"/></svg>
        oliver@kvars-club.example
      </li>
      <li>
        <svg viewBox="0 0 16 16" fill="none" stroke="#1e56b4" stroke-width="1.3"><circle cx="8" cy="8" r="6.5"/><ellipse cx="8" cy="8" rx="2.8" ry="6.5"/><line x1="1.5" y1="8" x2="14.5" y2="8"/></svg>
        www.kvars-club.example
      </li>
    </ul>

    <div class="address">42 Marwick Rd, Epsom<br>Auckland 1051</div>

    <svg class="footer-band" viewBox="0 0 620 22" preserveAspectRatio="none">
      <rect x="0" y="12" width="620" height="10" fill="var(--stripe-light)"/>
      <polygon points="448,22 456,0 620,0 620,22" fill="var(--paper)"/>
      <polygon points="452,22 460,2 620,2 620,22" fill="var(--stripe-dark)"/>
    </svg>
  </section>
</body>
</html>
```